Renewal of the Ferolanza SA Website

Ferolanza SA is a metal construction company active in industrial piping, boilermaking and metal framing. We would like to renew our site.

This website must be ready to work with Wordpress.

The site will contain the following pages: Home, skills, presentation, contact.

The site must reflect the field of the metal construction sector. It must be clear and easily understandable. The objective is not to win mandates with but to present the company and its capabilities.

I have inserted the pages of our old presentations, to describe our sector but we do not want to reuse these elements, we are waiting for your creativity to surprise us. In the 2nd phase we will complete with new images if necessary and texts

Target Market(s)

International companies in the food, chemical and pharmaceutical sectors

Industry/Entity Type

Alimentaire, pharma, chimie

Number of Pages Required

4 page

Font styles to use
Sans Serif

Colors
0054AA
0677BA
7BADD7
CADEEF
E8F1F8

Requirements
Must have
• It must contain at least the requested pages, images of illustrations, places for descriptions
Should not have
• Elements that appear or disappear, too flash,

```html
<!DOCTYPE html>
<html lang="fr">
<head>
<meta charset="utf-8">
<title>Ferolanza SA – Construction métallique</title>
<link rel="stylesheet" href="https://fonts.googleapis.com/css2?family=Roboto:wght@400;500;700;900&display=swap">
<style>
:root{
  --blue:#0054AA;
  --blue-2:#0677BA;
  --blue-3:#7BADD7;
  --blue-4:#CADEEF;
  --blue-5:#E8F1F8;
  --ink:#1b1f27;
  --muted:#5e6673;
  --line:#dfe5ec;
  --grey-bg:#eef2f6;
  --dark:#0f141c;
  --white:#ffffff;
}
*{box-sizing:border-box;margin:0;padding:0}
html,body{width:1200px;height:4744px;overflow:hidden}
body{font-family:"Roboto",Arial,sans-serif;color:var(--ink);background:var(--white);font-size:13px;line-height:1.6}
.wrap{width:1100px;margin:0 auto;position:relative}
.label{font-size:11px;font-weight:700;letter-spacing:2px;text-transform:uppercase;color:var(--blue)}
.label.center{display:flex;align-items:center;justify-content:center;gap:12px}
.label.center::before,.label.center::after{content:"";width:60px;height:1px;background:var(--blue-3)}
h2{font-size:34px;font-weight:500;line-height:1.2;color:var(--ink);letter-spacing:.5px}
.more{display:inline-flex;align-items:center;gap:6px;font-size:12px;font-weight:700;color:var(--blue)}
.more svg{width:14px;height:10px}
.btn{display:inline-flex;align-items:center;gap:8px;background:var(--blue);color:var(--white);font-size:12px;font-weight:700;padding:11px 22px;border-radius:2px}
.photo{position:relative}

/* Hero */
.hero{height:520px;position:relative;background:linear-gradient(120deg,#1a130d 0%,#3b2615 35%,#8a5426 62%,#2b2218 100%);color:var(--white)}
.hero .photo{position:absolute;inset:0}
.nav{position:absolute;top:0;left:0;right:0;height:40px;display:flex;align-items:center;padding:0 50px;border-bottom:1px solid rgba(255,255,255,.15)}
.brand{display:flex;align-items:center;gap:8px;font-weight:700;font-size:14px;color:var(--white)}
.brand i{display:block;width:22px;height:22px;border-radius:50%;background:var(--blue-2)}
.nav ul{list-style:none;display:flex;gap:26px;margin-left:auto;margin-right:30px;font-size:10px;font-weight:700;text-transform:uppercase;letter-spacing:.5px}
.nav ul li:first-child{color:var(--blue-3)}
.nav .btn{padding:7px 14px;font-size:10px}
.hero-text{position:absolute;left:50px;top:175px}
.hero-text .label{color:var(--white);font-size:13px;letter-spacing:3px}
.hero-text h1{font-size:54px;font-weight:700;line-height:1.05;margin:16px 0 30px}
.hero-text .more{color:var(--white)}

/* Features */
.features{margin-top:20px;display:grid;grid-template-columns:repeat(4,1fr);box-shadow:0 10px 30px rgba(0,0,0,.08)}
.feature{padding:32px 26px;height:200px;background:var(--white);border-right:1px solid var(--line)}
.feature h3{font-size:13px;font-weight:700;margin-bottom:10px}
.feature p{font-size:11px;color:var(--muted)}
.feature .ico{margin-top:14px;width:22px;height:22px;color:var(--blue)}
.feature.active{background:var(--blue);color:var(--white)}
.feature.active p{color:var(--blue-4)}
.feature.active .ico{color:var(--white)}

/* About */
.about{height:420px;padding-top:60px}
.about .wrap{display:flex;gap:40px}
.about-text{width:440px}
.about-text h2{margin:14px 0 22px;letter-spacing:1.5px}
.about-text p{color:var(--muted);font-size:12px;margin-bottom:14px}
.about .photo{flex:1;height:290px;margin-top:10px;background:linear-gradient(135deg,#e9edf1 0%,#b9c2cc 40%,#7e8894 70%,#dfe4ea 100%)}

/* Services */
.services{height:440px;padding-top:20px;text-align:center}
.services h2{margin:14px auto 50px;width:560px}
.svc-grid{display:grid;grid-template-columns:repeat(4,1fr);gap:40px;text-align:left}
.svc .circ{width:72px;height:72px;border-radius:50%;border:1px solid var(--blue-4);display:flex;align-items:center;justify-content:center;margin-bottom:18px}
.svc .circ svg{width:38px;height:38px;color:var(--blue)}
.svc:first-child .circ{background:var(--blue);border-color:var(--blue)}
.svc:first-child .circ svg{color:var(--white)}
.svc h3{font-size:15px;font-weight:700;margin-bottom:8px}
.svc p{font-size:11px;color:var(--muted);margin-bottom:12px}

/* Industries */
.industries{height:540px;padding-top:10px}
.industries h2{width:400px;margin-bottom:26px}
.ind-body{position:relative;height:400px}
.ind-body .photo{position:absolute;left:-50px;top:0;width:700px;height:400px;background:linear-gradient(100deg,#2a1a0e 0%,#7c4a1f 40%,#d3924b 70%,#4a3220 100%)}
.ind-card{position:absolute;left:570px;top:30px;width:380px;background:var(--blue);color:var(--white);padding:30px}
.ind-card h3{font-size:17px;font-weight:700;margin-bottom:14px}
.ind-card p{font-size:11px;color:var(--blue-4);margin-bottom:12px}
.ind-count{position:absolute;left:572px;top:352px;color:var(--white);font-size:22px;font-weight:700}
.ind-count small{font-size:11px;color:var(--blue-4)}
.ind-body .pipes{position:absolute;left:960px;top:290px;width:190px;height:110px;background:linear-gradient(135deg,#7bb3e0,#1d5fa5)}

/* Projects */
.projects{height:660px;background:var(--grey-bg);padding-top:50px}
.proj-head{display:flex;justify-content:space-between}
.proj-head h2{margin-top:10px}
.proj-head p{width:520px;font-size:11px;color:var(--muted);margin-bottom:10px}
.proj-grid{margin-top:30px;display:grid;grid-template-columns:repeat(3,1fr);gap:24px;position:relative}
.proj .photo{height:320px}
.proj:nth-child(1) .photo{background:linear-gradient(160deg,#e6c15a 0%,#7d7a70 40%,#3b3d44 100%)}
.proj:nth-child(2) .photo{background:linear-gradient(160deg,#c98a4c 0%,#6b4b36 45%,#2f2a27 100%)}
.proj:nth-child(3) .photo{background:linear-gradient(160deg,#f0a85a 0%,#8a5c3a 45%,#2a2e36 100%)}
.proj h4{font-size:15px;font-weight:500;margin-top:20px;line-height:1.3}
.proj:first-child h4{background:var(--white);padding:16px 20px;margin-top:0}
.badge{position:absolute;left:100px;top:110px;width:70px;height:70px;border-radius:50%;background:var(--blue);color:var(--white);font-size:11px;font-weight:700;display:flex;align-items:center;justify-content:center}
.arrow{position:absolute;top:200px;width:26px;height:26px;background:var(--white);display:flex;align-items:center;justify-content:center;color:var(--blue)}
.arrow.l{left:-40px}.arrow.r{right:-40px}
.arrow svg{width:12px;height:10px}

/* Why */
.why{margin-top:40px;height:380px;background:linear-gradient(100deg,#0d0f13 0%,#2a2520 45%,#7a5a3a 75%,#3a3a3c 100%);color:var(--white);padding-top:60px;position:relative}
.why .photo{position:absolute;inset:0}
.why .wrap{position:relative}
.why h2{color:var(--white);margin-bottom:22px}
.why p{width:560px;font-size:11px;color:#d6dbe2;margin-bottom:10px}
.why .more{color:var(--white);margin-top:6px}

/* Blog */
.blog{height:560px;padding-top:50px}
.blog-head{display:flex;justify-content:space-between;align-items:flex-end}
.blog-head h2{margin-top:10px}
.blog-head .btn{padding:7px 14px;font-size:10px}
.blog-grid{margin-top:30px;display:grid;grid-template-columns:repeat(3,1fr);gap:30px}
.post .photo{height:250px}
.post:nth-child(1) .photo{background:linear-gradient(150deg,#8d95a0,#3d4450 60%,#1f242b)}
.post:nth-child(2) .photo{background:linear-gradient(150deg,#2d3d5a,#c66a2a 50%,#1a1c22)}
.post:nth-child(3) .photo{background:linear-gradient(150deg,#e09a4a,#7a4a2a 50%,#2a2626)}
.date{position:absolute;right:14px;top:14px;width:38px;background:var(--blue);color:var(--white);font-size:9px;line-height:1.2;text-align:center;padding:6px 2px;font-weight:700}
.date b{display:block;font-size:15px}
.post h4{font-size:15px;font-weight:500;line-height:1.35;margin:18px 0 10px}

/* Contact */
.contact{height:460px;padding-top:20px;text-align:center}
.contact h2{margin:14px 0 16px}
.contact .lead{width:640px;margin:0 auto 30px;font-size:11px;color:var(--muted)}
.form{text-align:left;display:grid;grid-template-columns:1fr 1fr;gap:16px;width:940px;margin:0 auto}
.field{border:1px solid var(--line);height:42px;padding:12px 14px;font-size:11px;color:#8b93a0}
.field.area{grid-column:1/3;height:110px}
.form .btn{grid-column:1/3;justify-self:center;margin-top:10px}

/* Footer */
.footer{height:424px;background:var(--blue);color:var(--white);padding-top:60px}
.foot-grid{display:grid;grid-template-columns:320px 150px 230px 1fr;gap:40px}
.foot-grid p,.foot-grid li{font-size:11px;color:var(--blue-4)}
.foot-grid h5{font-size:13px;font-weight:700;margin-bottom:16px}
.foot-grid ul{list-style:none}
.foot-grid li{margin-bottom:8px;display:flex;gap:8px;align-items:center}
.foot-grid li svg{width:12px;height:12px;flex:none}
.foot-grid .brand{margin-bottom:20px}
.newsletter{display:flex;margin-top:14px}
.newsletter span{flex:1;background:var(--white);color:#8b93a0;font-size:11px;padding:10px 12px}
.newsletter b{background:var(--blue-2);width:42px;display:flex;align-items:center;justify-content:center}
.newsletter svg{width:14px;height:10px}
.foot-bottom{margin-top:80px;border-top:1px solid rgba(255,255,255,.2);padding-top:20px;display:flex;justify-content:space-between;font-size:11px;color:var(--blue-4)}
</style>
</head>
<body>

<header class="hero">
  <div class="photo" role="img" aria-label="Photo d'un soudeur en atelier métallique avec étincelles"></div>
  <nav class="nav">
    <div class="brand"><i></i>Ferolanza SA</div>
    <ul><li>Maison</li><li>À propos</li><li>Produits</li><li>Compétence</li><li>Présentation</li><li>Contactez-nous</li></ul>
    <span class="btn">Demander un devis →</span>
  </nav>
  <div class="hero-text">
    <div class="label">Une expertise inégalée</div>
    <h1>Nous construisons<br>votre rêve en</h1>
    <span class="more">Contactez-nous <svg viewBox="0 0 14 10"><path d="M0 5h12M8 1l4 4-4 4" stroke="currentColor" fill="none" stroke-width="1.6"/></svg></span>
  </div>
</header>

<section class="wrap features">
  <div class="feature"><h3>Sensibilité environnementale</h3><p>Nous limitons nos rejets et recyclons chaque chute d'acier de nos ateliers de fabrication.</p></div>
  <div class="feature"><h3>Tarification transparente</h3><p>Des offres détaillées et claires, sans frais cachés, pour chaque phase de votre projet.</p></div>
  <div class="feature active"><h3>Professionnel et Qualité</h3><p>Des équipes certifiées et des contrôles rigoureux à chaque étape de la production.</p>
    <svg class="ico" viewBox="0 0 24 24"><path d="M3 21h18M5 21V9l7-5 7 5v12M9 21v-6h6v6" stroke="currentColor" fill="none" stroke-width="1.5"/></svg></div>
  <div class="feature"><h3>Solutions personnalisées</h3><p>Chaque installation est conçue sur mesure selon les contraintes de votre site.</p></div>
</section>

<section class="about">
  <div class="wrap">
    <div class="about-text">
      <div class="label">À propos de nous</div>
      <h2>Nous Vous assurons la qualité et le respect des normes</h2>
      <p>Dans ce secteur, les entreprises les plus importantes au monde se fient à notre savoir-faire pour la tuyauterie et la construction métallique de précision.</p>
      <p>Ferolanza SA réunit des soudeurs, chaudronniers et monteurs expérimentés au service des industries alimentaire, chimique et pharmaceutique.</p>
      <span class="more">En savoir plus <svg viewBox="0 0 14 10"><path d="M0 5h12M8 1l4 4-4 4" stroke="currentColor" fill="none" stroke-width="1.6"/></svg></span>
    </div>
    <div class="photo" role="img" aria-label="Pile de tubes en acier inoxydable"></div>
  </div>
</section>

<section class="services">
  <div class="wrap">
    <div class="label center">Notre domaine de service</div>
    <h2>Notre service de construction actif dans ce domaine</h2>
    <div class="svc-grid">
      <div class="svc"><div class="circ"><svg viewBox="0 0 40 40"><path d="M8 30V14h10v12h14M8 14h10M26 20v12M32 20v12" stroke="currentColor" fill="none" stroke-width="2"/></svg></div>
        <h3>Tuyauterie industrielle</h3><p>Réseaux inox et acier pour fluides de process, montage et maintenance.</p><span class="more">En savoir plus →</span></div>
      <div class="svc"><div class="circ"><svg viewBox="0 0 40 40"><circle cx="20" cy="20" r="11" stroke="currentColor" fill="none" stroke-width="2"/><path d="M20 9v22M9 20h22" stroke="currentColor" stroke-width="2"/></svg></div>
        <h3>Chaudronnerie</h3><p>Cuves, réservoirs et pièces formées sur mesure dans nos ateliers.</p><span class="more">En savoir plus →</span></div>
      <div class="svc"><div class="circ"><svg viewBox="0 0 40 40"><path d="M6 32l28-24M12 32l22-18M6 26l20-18" stroke="currentColor" fill="none" stroke-width="2"/></svg></div>
        <h3>Charpente métallique</h3><p>Structures, passerelles et supports de conduites pour sites industriels.</p><span class="more">En savoir plus →</span></div>
      <div class="svc"><div class="circ"><svg viewBox="0 0 40 40"><path d="M8 30h24M14 30V18l8-8 6 6-8 8H14M26 8l4-2" stroke="currentColor" fill="none" stroke-width="2"/></svg></div>
        <h3>Soudage</h3><p>Soudage TIG, MIG et orbital certifié selon les normes en vigueur.</p><span class="more">En savoir plus →</span></div>
    </div>
  </div>
</section>

<section class="industries">
  <div class="wrap">
    <h2>Industries que nous servons</h2>
    <div class="ind-body">
      <div class="photo" role="img" aria-label="Salle de tuyauteries industrielles dans une usine chimique"></div>
      <div class="ind-card">
        <h3>Tuyauterie pour l'industrie chimique</h3>
        <p>Depuis plus de vingt ans, nos entreprises partenaires nous confient la conception et le montage de réseaux résistants aux fluides agressifs.</p>
        <p>C'est par la rigueur de nos soudeurs, la traçabilité des matériaux et le respect des normes que nous garantissons des installations sûres.</p>
        <p>La réputation de nos clients suffit à elle seule à décrire le privilège que nous donnent ces partenaires de longue date.</p>
      </div>
      <div class="ind-count">02<small>/06</small></div>
      <div class="pipes" role="img" aria-label="Tubes bleus empilés"></div>
    </div>
  </div>
</section>

<section class="projects">
  <div class="wrap">
    <div class="proj-head">
      <div><div class="label">Nos projets</div><h2>Nos projets réalisés</h2></div>
      <p>Dans un souci de qualité et de respect des normes, nos collaborateurs sont régulièrement formés. Nos équipes réalisent chaque année des chantiers exigeants pour des clients de renom, de la conception à la mise en service, avec un suivi complet de la documentation technique et des contrôles qualité.</p>
    </div>
    <div class="proj-grid">
      <span class="arrow l"><svg viewBox="0 0 12 10"><path d="M12 5H2M5 1L1 5l4 4" stroke="currentColor" fill="none" stroke-width="1.6"/></svg></span>
      <div class="proj"><div class="photo" role="img" aria-label="Ouvriers en casque devant des cadres métalliques"><span class="badge">Voir</span></div><h4>Fabrication de cadres métalliques</h4></div>
      <div class="proj"><div class="photo" role="img" aria-label="Charpente en acier au carbone dans un hall"></div><h4>Charpente en acier au carbone</h4></div>
      <div class="proj"><div class="photo" role="img" aria-label="Usine de chaudronnerie au coucher du soleil"></div><h4>Chaudronnerie</h4></div>
      <span class="arrow r"><svg viewBox="0 0 12 10"><path d="M0 5h10M7 1l4 4-4 4" stroke="currentColor" fill="none" stroke-width="1.6"/></svg></span>
    </div>
  </div>
</section>

<section class="why">
  <div class="photo" role="img" aria-label="Bobines de tôle d'acier dans un entrepôt"></div>
  <div class="wrap">
    <h2>Pourquoi choisir Ferolanza SA</h2>
    <p>Dans ce secteur, les entreprises les plus importantes au monde se fient à notre expérience et à la qualité de nos réalisations, grâce à une méthode éprouvée.</p>
    <p>Le travail de nos équipes repose sur des procédures claires, des matériaux certifiés et une planification précise. Chaque projet est suivi par un chef de chantier dédié, du premier relevé jusqu'à la réception finale des installations.</p>
    <p>La réputation de nos clients suffit à elle seule à décrire le privilège que nous donnent ces partenaires internationaux.</p>
    <span class="more">En savoir plus →</span>
  </div>
</section>

<section class="blog">
  <div class="wrap">
    <div class="blog-head">
      <div><div class="label">Blog</div><h2>Dernier blog et actualités</h2></div>
      <span class="btn">Voir plus →</span>
    </div>
    <div class="blog-grid">
      <div class="post"><div class="photo" role="img" aria-label="Installation de tuyauterie inox"><span class="date"><b>24</b>JUIN</span></div><h4>l'authenticité des produits alimentaires, nous s...</h4><span class="more">En savoir plus →</span></div>
      <div class="post"><div class="photo" role="img" aria-label="Soudeur au travail avec étincelles"><span class="date"><b>24</b>JUIN</span></div><h4>l'authenticité des produits alimentaires, nous s...</h4><span class="more">En savoir plus →</span></div>
      <div class="post"><div class="photo" role="img" aria-label="Atelier de métallerie éclairé"><span class="date"><b>24</b>JUIN</span></div><h4>l'authenticité des produits alimentaires, nous s...</h4><span class="more">En savoir plus →</span></div>
    </div>
  </div>
</section>

<section class="contact">
  <div class="wrap">
    <div class="label center">Contactez-nous</div>
    <h2>Commençons quelque chose de nouveau</h2>
    <p class="lead">La réputation de nos clients suffit à elle seule à décrire le privilège que nous donnent ces entreprises internationales et nos professionnels de la construction.</p>
    <div class="form">
      <div class="field">Entrez votre nom</div>
      <div class="field">Entrez votre identifiant de messagerie</div>
      <div class="field area">Entrez votre message</div>
      <span class="btn">Soumettre →</span>
    </div>
  </div>
</section>

<footer class="footer">
  <div class="wrap">
    <div class="foot-grid">
      <div><div class="brand"><i></i>Ferolanza SA</div>
        <p>Ferolanza SA est une entreprise de construction métallique active dans la tuyauterie industrielle, la chaudronnerie et la charpente pour l'industrie.</p></div>
      <div><h5>Liens rapides</h5><ul><li>À propos de nous</li><li>Nos services</li><li>Compétence</li><li>Présentation</li><li>Contactez-nous</li></ul></div>
      <div><h5>Contact Us</h5><ul>
        <li><svg viewBox="0 0 12 12"><path d="M2 1h3l1 3-2 1a7 7 0 003 3l1-2 3 1v3c-6 0-10-4-10-10z" fill="currentColor"/></svg>+41 27 555 04 18</li>
        <li><svg viewBox="0 0 12 12"><rect x="1" y="2" width="10" height="8" fill="none" stroke="currentColor"/><path d="M1 2l5 4 5-4" fill="none" stroke="currentColor"/></svg>info@ferolanza-metal.ch</li>
        <li><svg viewBox="0 0 12 12"><path d="M6 11S2 7 2 4.5a4 4 0 018 0C10 7 6 11 6 11z" fill="currentColor"/></svg>Rue des Forges 12, 1950 Sion</li></ul></div>
      <div><h5>Lettre d'information</h5><p>Inscrivez-vous pour recevoir nos dernières actualités et offres.</p>
        <div class="newsletter"><span>Adresse e-mail</span><b><svg viewBox="0 0 14 10"><path d="M0 5h12M8 1l4 4-4 4" stroke="#fff" fill="none" stroke-width="1.6"/></svg></b></div></div>
    </div>
    <div class="foot-bottom"><span>Copyright © 2024 Ferolanza SA. Tous droits réservés.</span><span>Politique de confidentialité · Termes et conditions</span></div>
  </div>
</footer>

</body>
</html>
```